BRV Coffee bag (front and back)

We use black matte bags and have front and back labels. We have a logo but need an attractive and inviting label. The labels will be used for our entire line of coffees. We sell most of our coffee to foodservice establishments (Restaurants, Hotels, Bakeries, Bodegas) and we would like to have these establishments display our bags of coffee to sell retail.
The logo can be used as a whole or using any one of the three components (Logo, image, tag).

Target Market(s)

People who buy the coffee they brew at home from the local shop they get their morning latte.. We are a local coffee company, but we do not sell locally roasted coffee!

Industry/Entity Type

Food

Font styles to use
Other font styles liked:
• something that looks good with our trademarked BRV

Colors

Designer to choose colors to be used in the design.

Requirements
Must have
• Respect Trademarked logo
Nice to have
• It would be nice to have a design that can be used with other mediums (airpot wraps, java jackets, )
Should not have
• Real People

```html
<!DOCTYPE html>
<html lang="en">
<head>
<meta charset="utf-8">
<title>BRV Coffee bag labels</title>
<link href="https://fonts.googleapis.com/css2?family=Montserrat:wght@400;500;600;700;800&display=swap" rel="stylesheet">
<style>
  :root {
    --bg: #cfd0d3;
    --label: #060607;
    --red: #ea222d;
    --white: #ffffff;
  }
  * { margin: 0; padding: 0; box-sizing: border-box; }
  html, body { width: 1200px; height: 931px; overflow: hidden; }
  body {
    background: var(--bg);
    font-family: "Montserrat", Arial, sans-serif;
    color: var(--white);
    position: relative;
  }
  .label {
    position: absolute;
    top: 129px;
    width: 419px;
    height: 671px;
    background: var(--label);
    overflow: hidden;
  }
  .label--front { left: 158px; }
  .label--back { left: 622px; }
  .label__arc { position: absolute; inset: 0; }
  .brand {
    position: absolute;
    left: 0; right: 0;
    top: 150px;
    text-align: center;
  }
  .brand__dot {
    width: 64px; height: 64px;
    border-radius: 50%;
    background: var(--red);
    margin: 0 auto 22px;
  }
  .brand__name {
    font-size: 72px;
    font-weight: 500;
    line-height: 1;
    letter-spacing: 4px;
  }
  .brand__tag {
    margin-top: 12px;
    font-size: 8px;
    font-weight: 500;
    letter-spacing: 3.2px;
  }
  .product {
    position: absolute;
    left: 73px;
    top: 440px;
    width: 272px;
  }
  .product__name {
    font-weight: 800;
    font-size: 44px;
    line-height: 0.98;
    letter-spacing: 0.5px;
  }
  .product__name span { display: block; }
  .product__name .wide { letter-spacing: 5px; }
  .product__desc {
    margin-top: 8px;
    border-top: 1.5px solid var(--white);
    border-bottom: 1.5px solid var(--white);
    padding: 6px 0 7px;
    color: var(--red);
    font-weight: 700;
    font-size: 12.5px;
    text-align: center;
    white-space: nowrap;
  }
  .product__meta {
    margin-top: 16px;
    display: flex;
    align-items: center;
    justify-content: space-between;
  }
  .roast { display: flex; align-items: center; gap: 8px; }
  .roast__dot { width: 30px; height: 30px; border-radius: 50%; background: var(--white); }
  .roast__text, .weight__text { font-weight: 700; font-size: 15px; line-height: 0.95; }
  .weight { display: flex; align-items: flex-end; gap: 3px; }
  .weight__num { font-weight: 700; font-size: 44px; line-height: 0.8; }
  .weight__unit { font-weight: 700; font-size: 15px; line-height: 1; margin-right: 4px; }
  .weight__text { font-size: 13px; line-height: 0.9; }
  .info {
    position: absolute;
    left: 0; right: 0;
    top: 410px;
    text-align: center;
  }
  .info__heading {
    color: var(--red);
    font-weight: 700;
    font-size: 19px;
    line-height: 1.2;
  }
  .info__list { list-style: none; font-size: 11.5px; font-weight: 500; line-height: 1.3; margin-bottom: 14px; }
  .info__list li::before { content: "• "; }
  .distributor__heading { font-weight: 700; font-size: 19px; margin-bottom: 8px; }
  .distributor__line { font-size: 12px; font-weight: 500; line-height: 1.3; }
</style>
</head>
<body>
  <section class="label label--front">
    <svg class="label__arc" viewBox="0 0 419 671" aria-hidden="true">
      <path d="M -20 420 Q 210 700 440 420" fill="none" stroke="#ea222d" stroke-width="44"/>
    </svg>
    <div class="brand">
      <div class="brand__dot"></div>
      <div class="brand__name">BRV</div>
      <div class="brand__tag">Bravo Roast Ventures</div>
    </div>
    <div class="product">
      <h1 class="product__name"><span>BOLD CREMA</span><span class="wide">ESPRESSO</span></h1>
      <p class="product__desc">A RICH, CLASSIC ESPRESSO BLEND.</p>
      <div class="product__meta">
        <div class="roast">
          <div class="roast__dot"></div>
          <div class="roast__text">ESPRESSO<br>ROAST</div>
        </div>
        <div class="weight">
          <span class="weight__num">2</span>
          <span class="weight__unit">LB</span>
          <span class="weight__text">WHOLE<br>BEAN<br>COFFEE</span>
        </div>
      </div>
    </div>
  </section>

  <section class="label label--back">
    <svg class="label__arc" viewBox="0 0 419 671" aria-hidden="true">
      <path d="M -20 420 Q 210 700 440 420" fill="none" stroke="#ea222d" stroke-width="44"/>
    </svg>
    <div class="brand">
      <div class="brand__dot"></div>
      <div class="brand__name">BRV</div>
      <div class="brand__tag">Bravo Roast Ventures</div>
    </div>
    <div class="info">
      <h2 class="info__heading">BREWING</h2>
      <ul class="info__list">
        <li>Use Fresh Filterd cold water.</li>
        <li>Measure 2 TBS of coffee for every 6oz of water.</li>
        <li>Brew with water 195-F-205-F.</li>
      </ul>
      <h2 class="info__heading">STORING</h2>
      <ul class="info__list">
        <li>Store in an airtight container in a cool, dry place.</li>
        <li>Do not freeze.</li>
      </ul>
      <div class="distributor">
        <h3 class="distributor__heading">Distributed by:</h3>
        <p class="distributor__line">Rivermark coffee company LLC</p>
        <p class="distributor__line">555-014-2290 info@rivermarkcoffee.com</p>
      </div>
    </div>
  </section>
</body>
</html>
```